Brava Helix Inc - Cutting-Edge Biotech Laboratory - Sleek & Sophisticated

Please design a website that has more of a high-tech and high-end feel, with contents outlined in the uploaded file.

Please have main tabs of the following categories: Home, About, FDA & LAWS, Science, Products, Media, Contact.

Media can include all the videos and photos.

Current website: www.bravahelixlabs.example - it needs to be much more high-end, sleek and more organized. Please do NOT follow the outlines in the old website, but follow the uploaded CONTENT file.

Target Market(s)

doctors

Industry/Entity Type

Biotechnology

Coding

Coded - Design and coding required

Number of Pages Required

5+ page

Requirements
Must have
• Logo
Nice to have
• Some lotion on the website

```html
<!DOCTYPE html>
<html lang="en">
<head>
<meta charset="utf-8">
<title>Brava Helix Inc — Regenerative Medicine</title>
<link href="https://fonts.googleapis.com/css2?family=Open+Sans:ital,wght@0,400;0,600;0,700;1,400;1,600&family=Roboto:wght@300;400;500;700&display=swap" rel="stylesheet">
<style>
:root{
  --blue:#1f6fc5;
  --blue-dark:#175aa3;
  --ink:#333a45;
  --muted:#8a909a;
  --line:#e3e6eb;
  --soft:#f4f5f8;
  --red:#d6453d;
  --white:#ffffff;
}
*{box-sizing:border-box;margin:0;padding:0}
html,body{width:1200px;height:3556px;overflow:hidden}
body{font-family:"Open Sans",Arial,sans-serif;color:var(--ink);background:var(--white);font-size:13px;line-height:1.6}
h1,h2,h3,h4{font-family:"Roboto",Arial,sans-serif;font-weight:400}
.wrap{width:1060px;margin:0 auto;position:relative}

/* header */
.site-header{height:112px;position:relative;border-bottom:1px solid var(--line)}
.topbar{position:absolute;right:0;top:0;height:32px;width:640px;background:var(--blue);color:var(--white);font-size:12px;display:flex;align-items:center;justify-content:flex-end;gap:26px;padding-right:70px;clip-path:polygon(24px 0,100% 0,100% 100%,0 100%)}
.topbar span{display:flex;align-items:center;gap:6px}
.brand{position:absolute;left:70px;top:34px;display:flex;align-items:center;gap:10px;font-family:"Roboto",sans-serif;font-weight:500;font-size:26px;color:var(--blue);letter-spacing:1px}
.brand i{width:30px;height:30px;border-radius:50%;background:var(--blue);display:block}
.main-nav{position:absolute;right:70px;top:56px;display:flex;gap:4px;font-family:"Roboto",sans-serif;font-size:12px;font-weight:500}
.main-nav a{padding:10px 14px;color:var(--ink);text-decoration:none}
.main-nav a.active{color:var(--blue);border-bottom:2px solid var(--blue)}

/* hero */
.hero{height:528px;position:relative;background:linear-gradient(180deg,#9fb4c8 0%,#c9d4dc 22%,#7c7a6e 45%,#b0622f 65%,#c9732e 78%,#6b5a45 100%)}
.hero-copy{position:absolute;left:0;right:0;top:190px;text-align:center;color:var(--white)}
.hero-copy h1{font-family:"Open Sans",sans-serif;font-style:italic;font-weight:600;font-size:34px;line-height:1.25;text-shadow:0 2px 8px rgba(0,0,0,.35)}
.hero-copy p{font-size:13px;margin-top:10px;opacity:.95}
.hero-copy .btn-ghost{display:inline-block;margin-top:18px;padding:7px 24px;border:1px solid var(--white);border-radius:3px;font-size:11px;font-weight:600;letter-spacing:1px}

/* common section titles */
.eyebrow{color:var(--blue);font-size:13px}
.section-title{font-size:32px;color:var(--ink);margin-top:2px;padding-bottom:12px;position:relative}
.section-title::after{content:"";position:absolute;left:0;bottom:0;width:50px;height:2px;background:var(--blue)}
.centered{text-align:center}
.centered .section-title::after{left:50%;margin-left:-25px}
.lead{color:var(--muted);font-size:12px;margin-top:14px;max-width:520px}
.centered .lead{margin-left:auto;margin-right:auto}

/* about */
.about{height:380px;padding-top:56px}
.about .wrap{display:flex;justify-content:space-between}
.about-text{width:600px}
.about-text p{color:var(--muted);font-size:12px;margin-top:16px}
.btn-row{display:flex;gap:16px;margin-top:26px}
.btn{display:inline-block;padding:8px 26px;font-size:12px;border-radius:3px;font-weight:600}
.btn-solid{background:var(--blue);color:var(--white)}
.btn-outline{border:1px solid var(--line);color:var(--muted)}
.about-photo{width:380px;height:240px;margin-top:40px;background:linear-gradient(135deg,#e9eef3,#bcc9d6 60%,#8aa3bb)}

/* services */
.services{height:580px;background:var(--soft);padding-top:46px}
.services-body{display:flex;gap:60px;margin-top:40px}
.service-tabs{width:230px;list-style:none}
.service-tabs li{display:flex;align-items:center;gap:14px;height:56px;padding-left:12px;font-size:12px;color:var(--muted)}
.service-tabs li.active{background:var(--white);color:var(--ink);box-shadow:0 1px 4px rgba(0,0,0,.06)}
.service-tabs li i{width:30px;height:30px;border-radius:50%;background:linear-gradient(135deg,#2c7ccf,#0d3f7a);display:block}
.service-panel{flex:1}
.service-panel h3{font-size:22px}
.service-panel p{color:var(--muted);font-size:12px;margin-top:12px}
.details{color:var(--red);font-size:12px;margin-top:8px;display:block}
.service-gallery{display:flex;gap:24px;margin-top:18px}
.service-gallery div{width:230px;height:112px}

/* testimonials */
.testimonials{height:580px;padding-top:50px}
.quote-grid{display:grid;grid-template-columns:1fr 1fr;margin-top:40px;position:relative}
.quote-grid::before{content:"";position:absolute;left:50%;top:10px;bottom:10px;width:1px;background:var(--line)}
.quote-grid::after{content:"";position:absolute;top:50%;left:0;right:0;height:1px;background:var(--line)}
.quote{display:flex;gap:20px;align-items:center;padding:28px 34px;height:150px}
.quote p{color:var(--muted);font-size:12px;font-style:italic}
.quote .who{color:var(--ink);font-size:12px;margin-top:8px;font-style:normal;text-align:center}
.avatar{width:64px;height:64px;border-radius:50%;flex:none;background:linear-gradient(135deg,#c9b7a6,#6f5b4c)}

/* news */
.news{height:640px;background:#f7f8fa;padding-top:50px}
.news-grid{display:grid;grid-template-columns:repeat(4,1fr);gap:20px;margin-top:34px}
.news-card{background:var(--white);border:1px solid var(--line)}
.news-card .thumb{height:170px}
.news-card .body{padding:14px 16px}
.news-card h4{font-size:18px;color:var(--ink)}
.news-card p{color:var(--muted);font-size:11px;margin-top:6px}
.news-meta{display:flex;justify-content:space-between;border-top:1px solid var(--line);padding:9px 16px;font-size:11px;color:var(--muted)}

/* offices */
.offices{height:340px;padding-top:50px;border-top:1px solid var(--line)}
.office-cols{display:grid;grid-template-columns:1.3fr 1fr 1fr;gap:40px}
.col-title{font-size:16px;font-weight:500;padding-bottom:10px;border-bottom:1px solid var(--line);position:relative;margin-bottom:18px}
.col-title::after{content:"";position:absolute;left:0;bottom:-1px;width:40px;height:2px;background:var(--blue)}
.contact-pair{display:grid;grid-template-columns:1fr 1fr;gap:14px 30px;font-size:11px;color:var(--muted)}
.contact-pair strong{color:var(--ink);display:block;font-weight:600}

/* contact strip */
.contact{height:330px;background:var(--soft);padding-top:40px}
.contact-cols{display:grid;grid-template-columns:1fr 1.4fr 1fr;gap:40px}
.mail-form{display:grid;grid-template-columns:1fr 1fr;gap:8px}
.field{height:30px;background:var(--white);border:1px solid var(--line);font-size:11px;color:var(--muted);padding:6px 10px}
.field.full{grid-column:1/3}
.field.area{height:80px}
.send{grid-column:1/2;background:var(--blue);color:var(--white);font-size:11px;font-weight:600;text-align:center;padding:7px 0;border-radius:3px;margin-top:4px}
.map{height:210px;background:linear-gradient(135deg,#e7ebe3,#d3ddd0 50%,#cfdbe6)}
.contact-info p{font-size:11px;color:var(--muted);margin-bottom:8px}
.contact-info b{color:var(--ink);font-weight:600}
.follow{font-size:14px;margin-top:14px;color:var(--ink);font-family:"Roboto",sans-serif}
.socials{display:flex;gap:8px;margin-top:8px}
.socials i{width:24px;height:24px;border-radius:50%;background:var(--blue);display:block}

.copyright{height:66px;display:flex;align-items:center;justify-content:center;font-size:11px;color:var(--muted);border-top:1px solid var(--line)}
</style>
</head>
<body>

<header class="site-header">
  <div class="topbar">
    <span><svg width="12" height="12" viewBox="0 0 24 24" fill="#fff"><path d="M6.6 10.8a15 15 0 0 0 6.6 6.6l2.2-2.2c.3-.3.7-.4 1-.2 1.1.4 2.3.6 3.6.6.6 0 1 .4 1 1V20c0 .6-.4 1-1 1A17 17 0 0 1 3 4c0-.6.4-1 1-1h3.5c.6 0 1 .4 1 1 0 1.3.2 2.5.6 3.6.1.3 0 .7-.2 1z"/></svg>+1 (555) 014 2280</span>
    <span><svg width="12" height="12" viewBox="0 0 24 24" fill="#fff"><path d="M2 5h20v14H2z" opacity=".0"/><path d="M3 5h18v14H3zm2 2v.5l7 4.5 7-4.5V7z"/></svg>hello@bravahelixlabs.example</span>
  </div>
  <div class="brand"><i></i>BRAVA HELIX</div>
  <nav class="main-nav">
    <a class="active">HOME</a><a>ABOUT US</a><a>FDA &amp; LAWS</a><a>SCIENCE</a><a>PRODUCTS</a><a>MEDIA</a><a>CONTACT US</a>
  </nav>
</header>

<section class="hero" role="img" aria-label="Wide landscape photograph of a river valley with autumn foliage and snowy mountains">
  <div class="hero-copy">
    <h1>Leader in Regenerative Medicine<br>Innovator of the Industry</h1>
    <p>Stem cell science for healthy living</p>
    <span class="btn-ghost">LEARN MORE</span>
  </div>
</section>

<section class="about">
  <div class="wrap">
    <div class="about-text">
      <div class="eyebrow">About Us</div>
      <h2 class="section-title">Who we are ?</h2>
      <p>Brava Helix Inc is a biotechnology company focused on stem cell and regenerative therapies. Our mission is to help physicians give patients a better quality of life through safe, tested and well documented cell products made in certified laboratories.</p>
      <p>Over the past ten years of development, our team has carefully studied research from leading clinics and universities. We believe the body holds the power to heal itself, and our work is to support that process with care, precision and proven science for doctors everywhere.</p>
      <div class="btn-row"><span class="btn btn-solid">Contact Us</span><span class="btn btn-outline">Read More</span></div>
    </div>
    <div class="about-photo" role="img" aria-label="Photo of a team of scientists in white lab coats working together"></div>
  </div>
</section>

<section class="services">
  <div class="wrap">
    <div class="eyebrow">Services</div>
    <h2 class="section-title">What we do ?</h2>
    <p class="lead">We support doctors with research, compliant products and clear guidance on every step of regenerative care.</p>
    <div class="services-body">
      <ul class="service-tabs">
        <li class="active"><i></i>FDA &amp; LAWS</li>
        <li><i></i>Tissue Banks</li>
        <li><i></i>Orthopedics</li>
        <li><i></i>Diseases</li>
        <li><i></i>Classes of growth factors</li>
      </ul>
      <div class="service-panel">
        <h3>FDA &amp; LAWS</h3>
        <p>Our products are processed under strict federal guidelines. Every batch is screened, tested and tracked from donor to clinic, so physicians can treat patients with full confidence in safety, quality and legal compliance at every stage of care.</p>
        <p>We keep doctors informed about current regulations and changes in the field, and provide documents that make each step simple and clear.</p>
        <span class="details">Details »</span>
        <div class="service-gallery">
          <div role="img" aria-label="Photo of a patient receiving a treatment" style="background:linear-gradient(135deg,#e6d3c6,#b99b88)"></div>
          <div role="img" aria-label="Blue microscopic cell illustration" style="background:linear-gradient(135deg,#5fb4e6,#0b4f8f)"></div>
          <div role="img" aria-label="Photo of a laboratory sample in gloved hands" style="background:linear-gradient(135deg,#e9dcd2,#a98e7c)"></div>
        </div>
      </div>
    </div>
  </div>
</section>

<section class="testimonials">
  <div class="wrap centered">
    <div class="eyebrow">Testimonials</div>
    <h2 class="section-title">What Our Client Says ?</h2>
    <p class="lead">Doctors who work with us share what the partnership has meant for their clinics and their patients.</p>
    <div class="quote-grid">
      <div class="quote"><div><p>Our patients recovered faster than we expected. The support team answered every question and the paperwork was always ready on time. A reliable partner for our practice.</p><div class="who">Nico Hale, Operations Manager</div></div><div class="avatar" role="img" aria-label="Portrait photo of client"></div></div>
      <div class="quote"><div class="avatar" role="img" aria-label="Portrait photo of client"></div><div><p>Clear science, careful handling and honest advice. We trust the products and our team feels confident offering these treatments to patients who need them.</p><div class="who">Ivy Stroud, Creative Designer</div></div></div>
      <div class="quote"><div><p>The training sessions were practical and easy to follow. Within weeks our clinic added new services and the feedback from patients has been very positive.</p><div class="who">Petra Lund, Manager</div></div><div class="avatar" role="img" aria-label="Portrait photo of client"></div></div>
      <div class="quote"><div class="avatar" role="img" aria-label="Portrait photo of client"></div><div><p>Fast delivery, consistent quality and a team that truly cares. Working with this lab has made regenerative care a real part of how we help people.</p><div class="who">Sam Orrin, Developer</div></div></div>
    </div>
  </div>
</section>

<section class="news">
  <div class="wrap">
    <div class="eyebrow">Media</div>
    <h2 class="section-title">Latest News &amp; Views</h2>
    <p class="lead">Updates from our labs, clinics and partners, with new videos and photos added each month.</p>
    <div class="news-grid">
      <article class="news-card"><div class="thumb" role="img" aria-label="Photo of a lab hallway" style="background:linear-gradient(135deg,#c9b49d,#6e5a48)"></div><div class="body"><h4>Standard Post</h4><p>New study shows strong results for joint repair in older patients treated this year.</p></div><div class="news-meta"><span>20 June 2016</span><span>3</span></div></article>
      <article class="news-card"><div class="thumb" role="img" aria-label="Video still of lab glassware" style="background:linear-gradient(135deg,#efe9e2,#b9a99a)"></div><div class="body"><h4>Video Post</h4><p>Watch how our team prepares each sample in a clean and certified room.</p></div><div class="news-meta"><span>20 June 2016</span><span>5</span></div></article>
      <article class="news-card"><div class="thumb" role="img" aria-label="Photo of a doctor consulting a patient" style="background:linear-gradient(135deg,#d8c7b4,#5d5048)"></div><div class="body"><h4>Post with image</h4><p>A visit to a partner clinic where new therapies are changing daily care.</p></div><div class="news-meta"><span>20 June 2016</span><span>2</span></div></article>
      <article class="news-card"><div class="thumb" role="img" aria-label="Photo of a wooden interior" style="background:linear-gradient(135deg,#b78a5c,#5a3a22)"></div><div class="body"><h4>Image Post</h4><p>Photos from our annual meeting with doctors and research partners.</p></div><div class="news-meta"><span>20 June 2016</span><span>4</span></div></article>
    </div>
  </div>
</section>

<section class="offices">
  <div class="wrap office-cols">
    <div>
      <h4 class="col-title">Doctors Offices</h4>
      <div class="contact-pair">
        <div><strong>Dr. Alan Marsh</strong>118 Cedar Lane<br>Fresno, CA 93701</div>
        <div><strong>Dr. Ruth Vell</strong>42 Harbor Street<br>Salem, TX 77801</div>
        <div><strong>Dr. Owen Tarly</strong>9 Maple Road<br>Westfield, MI 48301</div>
        <div><strong>Dr. Lena Corvo</strong>27 Birch Avenue<br>Dover, OH 44101</div>
      </div>
    </div>
    <div>
      <h4 class="col-title">Chief</h4>
      <div class="contact-pair">
        <div><strong>Mara Quill</strong>Chief Scientist<br>+1 (555) 014 2281</div>
        <div><strong>Theo Brandt</strong>Lab Manager<br>+1 (555) 014 2282</div>
      </div>
    </div>
    <div>
      <h4 class="col-title">Headquarters</h4>
      <div class="contact-pair">
        <div><strong>Texas</strong>400 West Ridge Road<br>Plainfield, TX 75001</div>
        <div><strong>Email</strong>hello@bravahelixlabs.example</div>
      </div>
    </div>
  </div>
</section>

<section class="contact">
  <div class="wrap contact-cols">
    <div>
      <h4 class="col-title">Feel Free to Mail</h4>
      <div class="mail-form">
        <div class="field">Name*</div><div class="field">Email*</div>
        <div class="field full">Subject</div>
        <div class="field full area">Write Your Message Here...</div>
        <div class="send">SEND MESSAGE</div>
      </div>
    </div>
    <div>
      <h4 class="col-title">HQ Satellite</h4>
      <div class="map" role="img" aria-label="Street map showing the headquarters location"></div>
    </div>
    <div class="contact-info">
      <h4 class="col-title">Contact Info</h4>
      <p>Reach our team any weekday for product, training or order questions.</p>
      <p><b>Phone:</b> +1 (555) 014 2280</p>
      <p><b>Office:</b> 400 West Ridge Road, Plainfield</p>
      <p><b>Email:</b> hello@bravahelixlabs.example</p>
      <div class="follow">Follow Us on</div>
      <div class="socials"><i></i><i></i><i></i><i></i><i></i></div>
    </div>
  </div>
</section>

<footer class="copyright">© 2016 Brava Helix Inc. All Rights Reserved · www.bravahelixlabs.example</footer>

</body>
</html>
```